Carrowell Business Card Re-design

Our current cards are outdated. This is our website www.carrowellinsights.example. We would like something that is "on-brand" and consistent with our social media sites. We are strategic consultants with a core competency in Marketing Research. Although, please know we are considering a brand logo redesign and potentially a new look. If we like your work here we will invite you to participate when we get to that project. Thank you very much. Harriet
Here are our social sites: https://twitter.com/Carrowell?lang=en
https://plus.google.com/+Carrowellinsights
https://www.linkedin.com/company/5094827/
https://www.facebook.com/CarrowellInc/
Business

```html
<!DOCTYPE html>
<html lang="en">
<head>
<meta charset="utf-8">
<title>Carrowell Business Card</title>
<link rel="stylesheet" href="https://fonts.googleapis.com/css2?family=Jost:wght@400&family=Oswald:wght@300&family=Questrial&display=swap">
<style>
  :root {
    --brand-green: #8dc63f;
    --paper: #ffffff;
    --ink: #231f20;
    --muted: #a7a9ac;
    --frame: #c4c4c4;
  }
  html, body {
    margin: 0;
    padding: 0;
    width: 1200px;
    height: 1200px;
    overflow: hidden;
    background: var(--paper);
  }
  .sheet {
    position: relative;
    width: 1200px;
    height: 1200px;
    font-family: "Questrial", sans-serif;
    color: var(--ink);
  }
  .spec-label {
    position: absolute;
    font-family: "Questrial", sans-serif;
    font-size: 32px;
    letter-spacing: 1px;
    line-height: 1;
    color: var(--ink);
    white-space: nowrap;
  }
  .spec-label--top { left: 444px; top: 199px; }
  .spec-label--side { left: 912px; top: 457px; }
  .spec-arrow { position: absolute; }
  .spec-arrow--down { left: 451px; top: 246px; }
  .spec-arrow--left { left: 872px; top: 464px; }

  .card {
    position: absolute;
    left: 353px;
    width: 494px;
    height: 282px;
    box-sizing: border-box;
  }
  .card--front {
    top: 289px;
    background: var(--brand-green);
  }
  .card--back {
    top: 629px;
    background: var(--paper);
    border: 2px solid var(--frame);
  }
  .wordmark {
    position: absolute;
    left: 0;
    right: 0;
    text-align: center;
    font-family: "Jost", sans-serif;
    font-weight: 400;
    line-height: 1;
    letter-spacing: -0.5px;
  }
  .card--front .wordmark {
    top: 113px;
    font-size: 50px;
    color: var(--paper);
  }
  .card--back .wordmark {
    top: 36px;
    font-size: 82px;
    color: var(--brand-green);
  }
  .holder {
    position: absolute;
    right: 306px;
    top: 152px;
    text-align: right;
  }
  .holder__name {
    font-family: "Oswald", sans-serif;
    font-weight: 300;
    font-size: 17px;
    letter-spacing: 2px;
    color: var(--muted);
    line-height: 1;
  }
  .holder__role {
    margin-top: 5px;
    font-family: "Oswald", sans-serif;
    font-weight: 300;
    font-size: 12px;
    letter-spacing: 1px;
    color: var(--muted);
    line-height: 1;
  }
  .contact {
    position: absolute;
    left: 218px;
    top: 155px;
    margin: 0;
    padding: 0;
    list-style: none;
    font-size: 11.5px;
    letter-spacing: 0.3px;
    line-height: 17.6px;
    color: var(--muted);
    white-space: nowrap;
  }
  .contact__web { color: var(--brand-green); }
</style>
</head>
<body>
<main class="sheet">
  <div class="spec-label spec-label--top">UV Barnish</div>
  <svg class="spec-arrow spec-arrow--down" width="12" height="30" viewBox="0 0 12 30" aria-hidden="true">
    <line x1="6" y1="0" x2="6" y2="24" stroke="#231f20" stroke-width="1.6"/>
    <path d="M2 22 L6 29 L10 22 Z" fill="#231f20"/>
  </svg>

  <div class="spec-label spec-label--side">UV Barnish</div>
  <svg class="spec-arrow spec-arrow--left" width="30" height="12" viewBox="0 0 30 12" aria-hidden="true">
    <line x1="6" y1="6" x2="30" y2="6" stroke="#231f20" stroke-width="1.6"/>
    <path d="M8 2 L1 6 L8 10 Z" fill="#231f20"/>
  </svg>

  <section class="card card--front" aria-label="Card front">
    <div class="wordmark">carrowell</div>
  </section>

  <section class="card card--back" aria-label="Card back">
    <div class="wordmark">carrowell</div>
    <div class="holder">
      <div class="holder__name">NAME LASTNAME</div>
      <div class="holder__role">Position</div>
    </div>
    <ul class="contact">
      <li>tel: +1 555-214-0396</li>
      <li>email: info@carrowellinsights.example</li>
      <li class="contact__web">www.carrowellinsights.example</li>
      <li>418 Harbor Point Ave, Ste 200B</li>
      <li>Westbrook (Oregon)</li>
    </ul>
  </section>
</main>
</body>
</html>
```